High End Craft Beer needs a label design update

We would like to update the design of our line of craft beer, named Louis-Benoît. The brand name needs to stay predominant in the design. We initially launched with 2 flavours, but with the addition of the third product, we feel there is not enough differentiation between each flavour, and customers are confused in which flavour they are buying (BELGIAN WHITE, INDIA PALE ALE, and AMBER ALE are the current flavours).

We plan to launch a BLONDE LAGER product, but need the 4 products to be more differentiated between each other.

We are looking for the design of the 3 current products (and also the BLOND LAGER if possible) that would be more differentiated.
Updates

Reason: Hello, I am still looking for options, so I am extending the dead-line by 5 days. Thanks

Target Market(s)

Males (75%), 21 to 40.

Font styles to use
Serif
Sans Serif

Requirements
Must have
• All 4 labels need to be coherent between themselves, but more differentiated than the current design
Should not have
• We don't want to completely "re-brand" the product, as customers currently really like the products and its design. And current customers need to easily "recognize" the product they like at store level. The only problem is the confusion between the flavours.

```html
<!DOCTYPE html>
<html lang="fr">
<head>
<meta charset="utf-8">
<title>Louis-Benoît India Pale Ale – Label</title>
<link rel="stylesheet" href="https://fonts.googleapis.com/css2?family=Bebas+Neue&family=Libre+Baskerville&family=Marcellus&family=Montserrat:wght@800&family=Oswald:wght@500;700&display=swap">
<style>
  :root {
    --label-green: #0f5a3b;
    --ornament-tint: #cfe3d8;
    --ink: #231f20;
    --paper: #ffffff;
  }
  html, body {
    margin: 0;
    padding: 0;
    width: 935px;
    height: 1200px;
    overflow: hidden;
    background: var(--paper);
  }
  .label {
    position: relative;
    width: 935px;
    height: 1200px;
  }
  .label-shapes {
    position: absolute;
    inset: 0;
  }
  .corner-flag {
    font-family: "Marcellus", serif;
    font-size: 30px;
    letter-spacing: 10px;
    fill: var(--paper);
  }
  .brewery-arc-text {
    font-family: "Libre Baskerville", serif;
    font-size: 11px;
    letter-spacing: 1px;
    fill: var(--ink);
  }
  .brand-name {
    position: absolute;
    left: 0;
    width: 935px;
    margin: 0;
    text-align: center;
    font-family: "Bebas Neue", sans-serif;
    font-weight: 400;
    font-size: 74px;
    line-height: 1;
    letter-spacing: 20px;
    text-indent: 20px;
    color: var(--paper);
    -webkit-text-stroke: 2.5px var(--ink);
    text-shadow: 4px 4px 0 var(--ink);
  }
  .brand-name--first { top: 560px; }
  .brand-name--second { top: 650px; }
  .flavour-name {
    position: absolute;
    left: 0;
    top: 728px;
    width: 935px;
    margin: 0;
    text-align: center;
    font-family: "Marcellus", serif;
    font-size: 31px;
    letter-spacing: 3px;
    color: var(--paper);
    transform: rotate(-2deg);
    transform-origin: 478px 20px;
  }
  .origin-line {
    position: absolute;
    left: 0;
    top: 786px;
    width: 935px;
    margin: 0;
    text-align: center;
    font-family: "Libre Baskerville", serif;
    font-size: 19px;
    letter-spacing: 3px;
    color: var(--ink);
  }
  .strength-line {
    position: absolute;
    left: 0;
    top: 812px;
    width: 935px;
    margin: 0;
    text-align: center;
    font-family: "Montserrat", sans-serif;
    font-weight: 800;
    font-size: 18px;
    letter-spacing: 3px;
    color: var(--ink);
  }
  .volume {
    position: absolute;
    left: 318px;
    top: 866px;
    margin: 0;
    font-family: "Oswald", sans-serif;
    font-weight: 700;
    font-size: 26px;
    line-height: 1;
    color: var(--ink);
  }
  .abv {
    position: absolute;
    left: 551px;
    top: 857px;
    margin: 0;
    font-family: "Oswald", sans-serif;
    font-weight: 500;
    line-height: 1;
    color: var(--ink);
  }
  .abv-value { display: block; font-size: 19px; }
  .abv-unit { display: block; font-size: 10px; margin-top: 3px; }
</style>
</head>
<body>
<main class="label">
  <svg class="label-shapes" width="935" height="1200" viewBox="0 0 935 1200">
    <path class="shield-outer" fill="var(--label-green)"
          d="M192 319 H754 V862 Q620 905 473 985 Q326 905 192 862 Z"/>
    <path class="shield-inner" fill="var(--paper)"
          d="M206 333 H740 V852 Q615 893 473 968 Q331 893 206 852 Z"/>
    <path class="shield-rule" fill="var(--paper)" stroke="var(--label-green)" stroke-width="3"
          d="M221 348 H725 V840 Q610 880 473 950 Q336 880 221 840 Z"/>

    <polygon class="corner-band" fill="var(--label-green)" points="300,348 358,348 221,460 221,408"/>
    <polygon class="corner-band" fill="var(--label-green)" points="588,348 646,348 725,408 725,460"/>
    <text class="corner-flag" x="282" y="404" text-anchor="middle" transform="rotate(-39 282 394)">IPA</text>
    <text class="corner-flag" x="666" y="404" text-anchor="middle" transform="rotate(39 666 394)">IPA</text>

    <rect class="crest-ornament" role="img" aria-label="Decorative green filigree crest"
          x="345" y="352" width="255" height="128" rx="10" fill="var(--ornament-tint)"/>

    <path class="brewery-arch" d="M300 550 Q473 430 646 550" fill="none" stroke="var(--label-green)" stroke-width="2"/>
    <path class="brewery-arch" d="M318 545 Q473 445 628 545" fill="none" stroke="var(--label-green)" stroke-width="1.2"/>
    <path id="brewery-arc" d="M340 548 Q473 476 606 548" fill="none"/>
    <text class="brewery-arc-text" text-anchor="middle">
      <textPath href="#brewery-arc" startOffset="50%">· BRASSERIE LE VIEUX QUAI ·</textPath>
    </text>

    <polygon class="ribbon-tail" fill="var(--label-green)" points="265,750 305,738 305,782 275,775 290,762"/>
    <polygon class="ribbon-tail" fill="var(--label-green)" points="710,765 652,728 652,772 695,778 680,770"/>
    <polygon class="ribbon-band" fill="var(--label-green)" points="298,736 658,716 660,760 300,782"/>

    <rect role="img" aria-label="Small fleur-de-lis emblem" x="302" y="789" width="13" height="15" fill="var(--label-green)"/>
    <rect role="img" aria-label="Small fleur-de-lis emblem" x="630" y="789" width="13" height="15" fill="var(--label-green)"/>

    <rect class="base-ornament" role="img" aria-label="Decorative green scrollwork flourish"
          x="418" y="842" width="114" height="94" rx="10" fill="var(--ornament-tint)"/>
  </svg>

  <h1 class="brand-name brand-name--first">LOUIS</h1>
  <h1 class="brand-name brand-name--second">BENOÎT</h1>
  <p class="flavour-name">INDIA PALE ALE</p>
  <p class="origin-line">BRASSÉE AU QUÉBEC</p>
  <p class="strength-line">BIÈRE FORTE STRONG BEER</p>
  <p class="volume">500 ML</p>
  <p class="abv"><span class="abv-value">6.2%</span><span class="abv-unit">ALC. VOL.</span></p>
</main>
</body>
</html>
```